Wandrift: Travel business card redesign

We need a clean elegant look for our cards featuring blue and orange. Look should communicate a sense of strong design and seem uncluttered. The company is Wandrift which means drift to wander. As in every trip is an drift to wander. Feel free to reinvent the logo or just tweak it. Colors should be blue like Caribbean waters and a saturated orange. Keep it clean and simple.
Please match the information in the sample uploaded but the sample is horrible -- a non-starter -- use for information only. also please add managing director to my name as title

Target Market(s)
potential clients, hotels, trade publications
Industry/Entity Type
Travel Industry
Contact Information for Business Card
as above
Requirements
Must have
- Font should be century gothic. Colors below are close but a but prefer lighter in each case.

```html
<!DOCTYPE html>
<html lang="en">
<head>
<meta charset="utf-8">
<title>Wandrift Business Card</title>
<link rel="stylesheet" href="https://fonts.googleapis.com/css2?family=Montserrat:wght@400;600&display=swap">
<style>
  :root {
    --backdrop: #3a3633;
    --card: #0d0d0d;
    --orange: #f28a2e;
    --blue: #5fb6e0;
    --text: #e6e6e6;
    --muted: #a8a8a8;
    --silver: #cfcfcf;
  }
  * { margin: 0; padding: 0; box-sizing: border-box; }
  html, body { width: 1200px; height: 900px; overflow: hidden; }
  body {
    background: var(--backdrop);
    font-family: "Montserrat", "Century Gothic", sans-serif;
    position: relative;
  }
  .card {
    position: absolute;
    top: 300px;
    width: 540px;
    height: 310px;
    background: var(--card);
    box-shadow: 0 10px 30px rgba(0,0,0,.5);
  }
  .card--front { left: 40px; }
  .card--back { left: 620px; }

  /* front */
  .brand {
    position: absolute;
    left: 40px;
    top: 122px;
  }
  .brand__name {
    font-weight: 600;
    font-size: 34px;
    color: var(--orange);
    line-height: 1;
  }
  .brand__tagline {
    margin-top: 8px;
    font-size: 13px;
    color: var(--muted);
    letter-spacing: .5px;
  }
  .details {
    position: absolute;
    left: 300px;
    top: 44px;
    color: var(--text);
    font-size: 13px;
    line-height: 1.45;
  }
  .person__name { font-weight: 600; font-size: 16px; }
  .person__first { color: var(--orange); }
  .person__last { color: var(--blue); }
  .person__title { margin-bottom: 20px; }
  .address { margin-bottom: 14px; }
  .contacts { list-style: none; }
  .contacts li { display: flex; align-items: center; gap: 10px; }
  .contacts svg { width: 12px; height: 12px; fill: var(--orange); flex: none; }

  /* back */
  .mark {
    position: absolute;
    top: 96px;
    width: 100%;
    text-align: center;
  }
  .mark__name {
    font-weight: 600;
    font-size: 44px;
    color: var(--silver);
    line-height: 1;
  }
  .mark__tagline {
    margin-top: 10px;
    font-size: 14px;
    color: var(--muted);
    letter-spacing: .5px;
  }
  .motto {
    position: absolute;
    bottom: 62px;
    width: 100%;
    text-align: center;
    font-size: 15px;
    letter-spacing: 1px;
    color: var(--silver);
  }
</style>
</head>
<body>
  <section class="card card--front">
    <div class="brand">
      <div class="brand__name">Wandrift</div>
      <div class="brand__tagline">drift to wander</div>
    </div>
    <div class="details">
      <div class="person__name"><span class="person__first">Liam</span> <span class="person__last">Varga</span></div>
      <div class="person__title">Managing Director</div>
      <div class="address">1450 Harbor Crest Way N,<br>Bayside, 90512</div>
      <ul class="contacts">
        <li><svg viewBox="0 0 12 12"><path d="M2.5 0.8l2 2-1 1.3c.7 1.6 1.8 2.7 3.4 3.4l1.3-1 2 2-1.3 1.7C5.5 10 2 6.5 0.8 2.1z"/></svg>877.55.DRIFT(37438)</li>
        <li><svg viewBox="0 0 12 12"><path d="M3 0h6v12H3zM4 1.5v8h4v-8z"/></svg>323.555.0142</li>
        <li><svg viewBox="0 0 12 12"><path d="M3 0h6v3h2v8H1V3h2zM4 1v2h4V1zM3 5v1.5h6V5zm0 2.5V9h6V7.5z"/></svg>310.555.0187</li>
        <li><svg viewBox="0 0 12 12"><circle cx="6" cy="6" r="6"/><path d="M1 6h10M6 1v10" stroke="#0d0d0d" stroke-width="1"/></svg>www.wandrift.com</li>
      </ul>
    </div>
  </section>

  <section class="card card--back">
    <div class="mark">
      <div class="mark__name">Wandrift</div>
      <div class="mark__tagline">drift to wander</div>
    </div>
    <div class="motto">A TRUSTED JOURNEY PARTNER</div>
  </section>
</body>
</html>
```